Create a landing page for my local business that I’m looking to advertise

I own an oriental rug repair, restoration and cleaning business.
I’m looking to rug advertising and i would like a very clear *******UX and UI design******* website designed.

pages that i need:
-Repair and restoration
-Cleaning
-Blocking
-Staircase rug installation
_about us
-homepage
-our story
-contact us
-estimate

Www.velborugs.example

Industry/Entity Type

Rug Industry, Antique and New Rug Repair restoration and cleaning

Number of Pages Required

5+ page

Font styles to use
Serif
Sans Serif
Script

Colors
6B429C
8869AF
B7A5CE
E3DAEB
F3F0F8

Requirements
Must have
• IT HAS TO PRESENT FINE RUG REPAIR, RESTORATION AND CLEANING.
Should not have
• I DONT WANT THE WEBSITE TO LOOK LIKE A GENERIC “CLEANING COMPANY”. WE ARE A HIGH END RUG REPAIR ,RESTORATION AND CLEANING COMPANY

```html
<!DOCTYPE html>
<html lang="en">
<head>
<meta charset="utf-8">
<title>Velbo Rugs — Oriental Rug Repair</title>
<link href="https://fonts.googleapis.com/css2?family=Rajdhani:wght@500;600;700&family=Josefin+Sans:wght@300;400;600&display=swap" rel="stylesheet">
<style>
:root{
  --plum:#6B429C;
  --lavender:#8869AF;
  --lilac:#B7A5CE;
  --haze:#E3DAEB;
  --mist:#F3F0F8;
  --plum-dark:#4a2c70;
  --ink:#222222;
  --body:#555555;
  --night:#241733;
  --white:#ffffff;
}
*{margin:0;padding:0;box-sizing:border-box}
html,body{width:1200px;height:4441px;overflow:hidden}
body{position:relative;background:var(--white);font-family:"Josefin Sans",sans-serif;color:var(--body)}
.abs{position:absolute}
.head{font-family:"Rajdhani",sans-serif;font-weight:700;color:var(--ink);text-transform:uppercase;line-height:1.28}
.btn{position:absolute;display:flex;align-items:center;justify-content:center;background:var(--plum);color:var(--white);font-family:"Rajdhani",sans-serif;font-weight:700;font-size:17px;text-transform:uppercase;box-shadow:-8px 8px 0 rgba(107,66,156,.2);border-radius:14px 0 0 0}
.btn.light{background:var(--haze);color:var(--plum)}
.copy{font-size:12px;line-height:26px;color:var(--body)}

/* top bar */
.topbar{left:540px;top:0;width:660px;height:38px;background:var(--plum);border-radius:0 0 0 14px;display:flex;align-items:center;font-size:13px;color:var(--white)}
.topbar span{display:flex;align-items:center;gap:6px;margin-left:44px}
.login{position:absolute;left:417px;top:0;width:131px;height:38px;background:var(--night);color:var(--white);display:flex;align-items:center;justify-content:center;gap:8px;font-weight:600;font-size:14px}

/* hero */
.hero{left:0;top:0;width:1200px;height:1030px}
.brand{left:112px;top:58px;font-size:40px;font-weight:400;color:var(--lilac);letter-spacing:2px}
.nav{left:0;top:72px;width:1200px;font-family:"Rajdhani",sans-serif;font-weight:600;font-size:15px;color:var(--white);text-transform:uppercase}
.nav span{position:absolute}
.social{position:absolute;width:34px;height:34px;border:1.5px solid var(--white);border-radius:50%}
.hero-title{left:0;top:312px;width:1200px;text-align:center;font-family:"Rajdhani",sans-serif;font-weight:700;font-size:58px;color:var(--white)}
.hero-sub{left:0;top:383px;width:1200px;text-align:center;font-size:22px;color:var(--white)}
.slides{left:44px;top:283px;color:var(--white);font-size:12px}

/* about */
.mist{left:0;top:1030px;width:1200px;height:496px;background:var(--mist)}
.framed{border-radius:40px 0 50px 0;overflow:hidden}
.label{font-family:"Rajdhani",sans-serif;font-weight:500;font-size:33px;color:var(--lavender)}

/* services */
.tile{position:absolute;width:391px;height:376px}
.feature{background:rgba(107,66,156,.9);display:flex;flex-direction:column;align-items:center;justify-content:center;text-align:center;padding:0 34px}
.feature h3{font-family:"Rajdhani",sans-serif;font-weight:700;font-size:27px;color:var(--white);margin-bottom:14px}
.feature p{font-size:12.5px;line-height:23px;color:var(--haze)}

/* care */
.care{left:0;top:2629px;width:1200px;height:543px;background:var(--haze)}

/* footer */
.band{left:0;top:3831px;width:1200px;height:610px;background:linear-gradient(180deg,var(--plum) 0%,var(--plum-dark) 100%)}
.links{left:0;top:4313px;width:1200px;text-align:center;color:var(--white);font-size:13px;font-weight:400}
</style>
</head>
<body>

<!-- HERO -->
<div class="abs hero">
  <svg width="1200" height="1030" viewBox="0 0 1200 1030" class="abs" style="left:0;top:0">
    <defs>
      <radialGradient id="heroTone" cx="50%" cy="40%" r="75%">
        <stop offset="0" stop-color="#8a4a22"/>
        <stop offset=".55" stop-color="#5a3a24"/>
        <stop offset="1" stop-color="#2b2419"/>
      </radialGradient>
    </defs>
    <rect width="1200" height="1030" fill="url(#heroTone)" role="img" aria-label="Close-up photo of a glass of tea resting on a woven oriental rug"/>
    <rect width="1200" height="1030" fill="rgba(36,23,51,.35)"/>
    <path d="M0 638 Q600 980 1200 715 L1200 1030 L0 1030 Z" fill="var(--plum)"/>
    <path d="M0 662 Q600 1012 1200 722 L1200 1030 L0 1030 Z" fill="var(--mist)"/>
    <line x1="600" y1="736" x2="600" y2="888" stroke="var(--lilac)" stroke-width="1.5"/>
    <circle cx="600" cy="736" r="14" fill="var(--white)" stroke="var(--lilac)" stroke-width="1"/>
    <circle cx="600" cy="736" r="5" fill="var(--plum)"/>
  </svg>
</div>

<div class="abs topbar">
  <span>
    <svg width="13" height="13" viewBox="0 0 24 24"><path d="M6.6 10.8a15 15 0 0 0 6.6 6.6l2.2-2.2a1 1 0 0 1 1-.25 11.4 11.4 0 0 0 3.6.57 1 1 0 0 1 1 1V20a1 1 0 0 1-1 1A17 17 0 0 1 3 4a1 1 0 0 1 1-1h3.5a1 1 0 0 1 1 1c0 1.25.2 2.45.57 3.57a1 1 0 0 1-.25 1z" fill="#fff"/></svg>
    CALL US: (555) 014-2288</span>
  <span style="margin-left:26px">
    <svg width="14" height="11" viewBox="0 0 24 18"><rect x="1" y="1" width="22" height="16" rx="2" fill="none" stroke="#fff" stroke-width="2"/><path d="M1 2l11 8 11-8" fill="none" stroke="#fff" stroke-width="2"/></svg>
    info@velborugs.example</span>
  <div class="login">Login
    <svg width="18" height="16" viewBox="0 0 24 24"><circle cx="13" cy="12" r="8" fill="none" stroke="#fff" stroke-width="2"/><path d="M3 12h10m-3-3 3 3-3 3" fill="none" stroke="#fff" stroke-width="2"/></svg>
  </div>
</div>

<div class="abs brand">VELBO RUGS</div>

<div class="abs nav">
  <span style="left:590px">Home</span>
  <span style="left:676px">Services</span>
  <span style="left:786px">About</span>
  <span style="left:879px">Contact</span>
  <div class="social" style="left:967px;top:-9px"></div>
  <div class="social" style="left:1009px;top:-9px"></div>
  <div class="social" style="left:1050px;top:-9px"></div>
</div>

<div class="abs slides">
  <div>01</div>
  <div style="position:absolute;left:10px;top:20px;width:1.5px;height:190px;background:#fff"></div>
  <div style="margin-top:208px">04</div>
</div>

<h1 class="abs hero-title">ORIENTAL RUG REPAIR</h1>
<p class="abs hero-sub">Authenticity and perfection.</p>
<div class="btn" style="left:484px;top:436px;width:231px;height:50px">Get a free estimate</div>

<!-- ABOUT -->
<div class="abs mist"></div>
<div class="abs" style="left:123px;top:953px;width:448px;height:505px;background:var(--plum);border-radius:40px 0 56px 0"></div>
<div class="abs framed" style="left:115px;top:945px;width:450px;height:505px;background:linear-gradient(135deg,#b7521f,#7a2f16 50%,#c4862e)" role="img" aria-label="Detailed view of a red and gold oriental rug pattern"></div>

<div class="abs label" style="left:598px;top:956px">ABOUT</div>
<h2 class="abs head" style="left:598px;top:1000px;font-weight:500;font-size:35px;line-height:44px;width:440px">30+ years of experience in rug restoration field</h2>
<p class="abs copy" style="left:598px;top:1108px;width:492px">Velbo Rugs is a leading and trusted brand for all oriental and antique rug repairs, not only by consumers, but by all Chicagoland's finest Oriental Rug dealers and designers. With more than 30-plus years of experience, we are proud to offer a wide range of services for all types of rugs, including fine Persian rugs, Afghan rugs, Pakistani rugs, wool rugs, Antique Rugs, Oriental Rugs, Shag and many others across the United States and all over the world.</p>
<p class="abs copy" style="left:598px;top:1276px;width:492px">Our repair, restoration and cleaning team specializes in high-quality antique rug restoration and repair, as well as wool &amp; silk rugs, from all over the world. Sometimes wear and tear can happen in high traffic areas.</p>
<div class="btn" style="left:603px;top:1377px;width:237px;height:52px">Read more</div>

<!-- SERVICES -->
<h2 class="abs head" style="left:0;top:1600px;width:1200px;text-align:center;font-size:50px;font-weight:600">Our <span style="color:var(--plum);font-weight:700">Services</span></h2>

<div class="tile" style="left:7px;top:1691px;background:linear-gradient(135deg,#6a6358,#b8aa92 55%,#4e3f33)" role="img" aria-label="Artisan hands re-weaving the fringe of a rug on a loom"></div>
<div class="tile" style="left:403px;top:1691px;background:linear-gradient(135deg,#8869AF,#6B429C)" role="img" aria-label="Faded photo of a rug workshop behind the service highlight"></div>
<div class="tile feature" style="left:403px;top:1691px">
  <h3>REPAIR AND RESTORATION</h3>
  <p>Lorem ipsum dolor sit amet, consectetur adipiscing elit, sed do eiusmod tempor incididunt ut labore et dolore magna aliqua. Ut enim ad minim veniam, quis nostrud exercitation ullamco laboris nisi ut aliquip ex ea commodo consequat.</p>
</div>
<div class="tile" style="left:800px;top:1691px;background:linear-gradient(135deg,#7b3a2c,#4a2a26 50%,#5f6b3b)" role="img" aria-label="Red tribal rug hanging outdoors among greenery"></div>
<div class="tile" style="left:7px;top:2076px;background:linear-gradient(135deg,#7a7670,#b35a2a 45%,#6b2d18)" role="img" aria-label="Wet cleaning vacuum nozzle moving across an orange rug"></div>
<div class="tile" style="left:403px;top:2076px;background:linear-gradient(135deg,#8b1c1e,#e8ddd0 50%,#7a1517)" role="img" aria-label="Red and cream Persian rug with white fringe"></div>
<div class="tile" style="left:800px;top:2076px;background:linear-gradient(135deg,#c9a24a,#3b3a34 50%,#d2b465)" role="img" aria-label="Gold bordered rug with a dark central field"></div>

<div class="btn" style="left:460px;top:2493px;width:281px;height:52px">View more services</div>

<!-- CARE -->
<div class="abs care"></div>
<div class="abs" style="left:488px;top:2622px;width:712px;height:550px;clip-path:polygon(176px 0,712px 0,712px 550px,0 550px);background:linear-gradient(160deg,#4a4d48,#5b4530 55%,#7a5a35)" role="img" aria-label="Living room with a wooden vintage radio cabinet, plants and a floor lamp"></div>
<h2 class="abs head" style="left:112px;top:2748px;width:440px;font-size:35px;line-height:44px;color:var(--plum-dark)">We care and respect the rugs we work on.</h2>
<p class="abs copy" style="left:112px;top:2842px;width:440px;color:#3a3342">With over 30 years of expertise in restoring and cleaning precious rugs, we feel we have a duty to bring each rug to its former glory whenever this is possible. We are a family-owned and -operated area rug repair and restoration firm near Chicago, specializing in Oriental Rug Cleaning, Antique Rug Repair, Sun Fade Damage, Rug Stain Removal and many more services. We use the best cleaning solutions for our hand-wash services, as well as wool and silk rugs.</p>
<div class="btn" style="left:119px;top:3015px;width:231px;height:50px;background:var(--plum-dark)">Get a free estimate</div>

<!-- PRECIOUS -->
<div class="abs" style="left:123px;top:3270px;width:446px;height:480px;background:var(--lavender);border-radius:40px 0 56px 0"></div>
<div class="abs framed" style="left:115px;top:3262px;width:450px;height:478px;background:linear-gradient(120deg,#6d3a1c,#2b2826 55%,#3a2f2a)" role="img" aria-label="Walnut veneer cabinet beside a wooden chair on a patterned rug"></div>
<h2 class="abs head" style="left:598px;top:3345px;width:520px;font-size:33px;line-height:43px">There is nothing more precious than <span style="color:var(--plum)">the original.</span></h2>
<p class="abs copy" style="left:598px;top:3440px;width:486px">We value authenticity and we built our name on restoring rugs by hand, bringing back to life and using pieces that are in your family for generations or that you invested in because you appreciate their craftsmanship. This is our contribution to keeping the authenticity in your homes, and teaching new generations about the value manual craftsmanship can build, to the state of calling it art.</p>
<div class="btn" style="left:603px;top:3594px;width:237px;height:51px">Get a free estimate</div>

<!-- CTA BAND & FOOTER -->
<div class="abs band"></div>
<h2 class="abs head" style="left:0;top:3905px;width:1200px;text-align:center;font-size:35px;line-height:47px;color:var(--white)">Antique rug repair | Oriental rug restoration |<br>Antique rug cleaning</h2>
<div class="btn light" style="left:441px;top:4022px;width:324px;height:50px">Get a free estimate today</div>

<svg class="abs" style="left:0;top:4100px" width="1200" height="341" viewBox="0 0 1200 341">
  <path d="M0 158 Q600 -80 1200 106 L1200 341 L0 341 Z" fill="var(--lilac)"/>
  <path d="M0 176 Q600 -50 1200 122 L1200 341 L0 341 Z" fill="var(--night)"/>
  <polygon points="600,12 660,42 660,102 600,132 540,102 540,42" fill="var(--white)" stroke="var(--lavender)" stroke-width="6"/>
  <polygon points="600,34 640,54 640,92 600,112 560,92 560,54" fill="var(--plum)"/>
  <g fill="var(--lavender)">
    <circle cx="519" cy="174" r="15"/>
    <circle cx="565" cy="174" r="15"/>
    <circle cx="612" cy="174" r="15"/>
    <circle cx="659" cy="174" r="15"/>
  </g>
</svg>

<div class="abs links">Home &nbsp;&nbsp;|&nbsp;&nbsp; Contact &nbsp;&nbsp;|&nbsp;&nbsp; Blog &nbsp;&nbsp;|&nbsp;&nbsp; Privacy Policy &nbsp;&nbsp;|&nbsp;&nbsp; Shipping &nbsp;&nbsp;/&nbsp;&nbsp; Return Policy &nbsp;&nbsp;|&nbsp;&nbsp; Terms of Service</div>
<div class="abs links" style="top:4357px;font-size:12px;color:var(--haze)">©2021 Velbo Rugs - All rights reserved</div>

</body>
</html>
```